Steady Harvest of Patrons Programme Graphic

Please refer to attached graphic.
I wish to redesign this graphic to represent a programme of work that we (Brinvo) deliver to our customers.
The design represents 9 steps ( 3 steps at each of 3 levels) and is all about implementing the 'Steady Harvest of Patrons'

I like the fact that the increasing business growth is evident when you are progressing through the stages, but the current graphic looks dated and the colours are not working.
I would also like to incorporate the SHP logo we have created.

Target Market(s)

IT Sector - businesses looking to grow

Industry/Entity Type

We are a digital marketing company

Requirements
Must have
• Clear, concise design
Should not have
• Design must not be complicated

```html
<!DOCTYPE html>
<html lang="en">
<head>
<meta charset="utf-8">
<title>Steady Harvest of Patrons – Programme Graphic</title>
<link rel="stylesheet" href="https://fonts.googleapis.com/css2?family=Oswald:wght@600&family=Poppins:wght@300;400;600;700&display=swap">
<style>
  :root {
    --stage: #cbcbcb;
    --card: #ffffff;
    --ink: #3a3b3f;
    --ground: #3d3e42;
    --title-from: #35c9fb;
    --title-to: #1390cf;
    --brand-blue: #1b9ad6;
    --panel-top: #e6e7e9;
    --panel-bottom: #ffffff;
    --fold: #a7a8ab;
    --arrow: #1a8fd9;
    --s1-from: #08b2e6; --s1-to: #18d2fb; --s1-tab: #078bb5;
    --s2-from: #0c73c3; --s2-to: #139ee8; --s2-tab: #075285;
    --s3-from: #1f55c6; --s3-to: #3397f0; --s3-tab: #07469a;
  }
  * { box-sizing: border-box; margin: 0; padding: 0; }
  html, body { width: 1200px; height: 890px; overflow: hidden; }
  body { background: var(--stage); position: relative; font-family: 'Poppins', sans-serif; color: var(--ink); }

  .card { position: absolute; left: 94px; top: 88px; width: 1012px; height: 714px; background: var(--card); }
  .ground { position: absolute; left: 94px; top: 786px; width: 1012px; height: 16px; background: var(--ground); z-index: 3; }

  .title-band { position: absolute; left: 94px; top: 162px; width: 781px; height: 72px;
    background: linear-gradient(90deg, var(--title-from), var(--title-to) 35%, var(--title-to)); }
  .title-band h1 { position: absolute; left: 65px; top: 50%; transform: translateY(-52%);
    font-family: 'Oswald', sans-serif; font-weight: 600; font-size: 47px; letter-spacing: 0.2px;
    color: #fff; text-transform: uppercase; white-space: nowrap; }

  .programme-mark { position: absolute; left: 890px; top: 168px; display: flex; align-items: center; gap: 10px; }
  .programme-mark .square { width: 30px; height: 30px; background: var(--brand-blue); }
  .programme-mark span { font-family: 'Poppins', sans-serif; font-weight: 700; font-size: 52px; color: var(--brand-blue); line-height: 1; }

  .axis { position: absolute; left: 159px; top: 273px; width: 6px; height: 513px; background: var(--ground); }
  .value-flag { position: absolute; left: 159px; top: 273px; width: 303px; height: 64px;
    background: linear-gradient(90deg, #38393c, #8d8e92);
    clip-path: polygon(0 0, 94% 0, 100% 50%, 94% 100%, 0 100%); }
  .value-flag span { position: absolute; left: 37px; top: 50%; transform: translateY(-50%);
    color: #fff; font-weight: 400; font-size: 28px; letter-spacing: 0.3px; white-space: nowrap; }

  .step { position: absolute; height: 87px; }
  .step .panel { position: absolute; left: 0; z-index: 1; background: linear-gradient(180deg, var(--panel-top), var(--panel-bottom)); }
  .step .fold { position: absolute; z-index: 1; width: 23px; height: 23px; background: var(--fold);
    clip-path: polygon(0 0, 100% 0, 0 100%); }
  .step .band { position: absolute; z-index: 2; left: 0; top: 0; height: 87px; }
  .step .tab { position: absolute; z-index: 2; left: 0; top: 0; height: 87px;
    clip-path: polygon(0 0, 68% 0, 100% 50%, 68% 100%, 0 100%); }
  .step .num { position: absolute; z-index: 2; top: 50%; transform: translateY(-50%);
    font-weight: 700; font-size: 36px; color: #fff; line-height: 1; }
  .step .heading { position: absolute; z-index: 2; top: 23px; color: #fff; white-space: nowrap; line-height: 1.2; }
  .step .heading strong { display: block; font-weight: 700; font-size: 17.5px; letter-spacing: 0.2px; text-transform: uppercase; }
  .step .heading em { display: block; font-style: normal; font-weight: 400; font-size: 17.5px; }
  .step ul { position: absolute; z-index: 2; list-style: none; }
  .step li { position: relative; font-size: 26px; font-weight: 400; color: #3b3c40; line-height: 42px; white-space: nowrap; }
  .step li::before { content: ""; position: absolute; left: -24px; top: 50%; width: 7px; height: 7px;
    border-top: 3px solid var(--arrow); border-right: 3px solid var(--arrow);
    transform: translateY(-50%) rotate(45deg); }

  .step-1 { left: 164px; top: 510px; }
  .step-1 .band { width: 344px; background: linear-gradient(90deg, var(--s1-from), var(--s1-to)); }
  .step-1 .tab { width: 62px; background: var(--s1-tab); }
  .step-1 .num { left: 6px; }
  .step-1 .heading { left: 83px; }
  .step-1 .panel { top: 87px; width: 321px; height: 176px; }
  .step-1 .fold { left: 321px; top: 87px; }
  .step-1 ul { left: 105px; top: 120px; }

  .step-2 { left: 427px; top: 414px; }
  .step-2 .band { width: 348px; background: linear-gradient(90deg, var(--s2-from), var(--s2-to)); }
  .step-2 .tab { width: 77px; background: var(--s2-tab); }
  .step-2 .num { left: 12px; }
  .step-2 .heading { left: 100px; }
  .step-2 .panel { top: 87px; width: 325px; height: 170px; }
  .step-2 .fold { left: 325px; top: 87px; }
  .step-2 ul { left: 123px; top: 111px; }

  .step-3 { left: 684px; top: 318px; }
  .step-3 .band { width: 359px; background: linear-gradient(90deg, var(--s3-from), var(--s3-to)); }
  .step-3 .tab { width: 77px; background: var(--s3-tab); }
  .step-3 .num { left: 12px; }
  .step-3 .heading { left: 106px; }
  .step-3 .panel { top: 87px; width: 336px; height: 177px; }
  .step-3 .fold { left: 336px; top: 87px; }
  .step-3 ul { left: 126px; top: 113px; }

  .company-name { position: absolute; left: 787px; top: 660px; font-family: 'Poppins', sans-serif;
    font-weight: 700; font-size: 62px; line-height: 1; color: var(--brand-blue); }
</style>
</head>
<body>
  <div class="card"></div>

  <div class="title-band"><h1>Steady Harvest of Patrons</h1></div>

  <div class="programme-mark"><div class="square"></div><span>SHP</span></div>

  <div class="axis"></div>
  <div class="value-flag"><span>BUSINESS VALUE</span></div>

  <section class="step step-1">
    <div class="panel"></div>
    <div class="fold"></div>
    <div class="band"></div>
    <div class="tab"></div>
    <span class="num">01</span>
    <div class="heading"><strong>Numbers That Matter</strong><em>Foundation Metrics</em></div>
    <ul><li>Personas</li><li>Database</li><li>Systems</li></ul>
  </section>

  <section class="step step-2">
    <div class="panel"></div>
    <div class="fold"></div>
    <div class="band"></div>
    <div class="tab"></div>
    <span class="num">02</span>
    <div class="heading"><strong>Weekly Scorecard</strong><em>Foundation Metrics</em></div>
    <ul><li>Messaging</li><li>Leads</li><li>Pipeline</li></ul>
  </section>

  <section class="step step-3">
    <div class="panel"></div>
    <div class="fold"></div>
    <div class="band"></div>
    <div class="tab"></div>
    <span class="num">03</span>
    <div class="heading"><strong>Monthly Scorecard</strong><em>Strategic Review</em></div>
    <ul><li>Sales</li><li>Nurture</li><li>Reference</li></ul>
  </section>

  <div class="company-name">Brinvo</div>

  <div class="ground"></div>
</body>
</html>
```